Bramble Fitness Flyer

Need a flyer to showcase my fitness facility with a focus on "PERSONAL TRAINING". To be used in paper advertisements.

I've added some photos below. Please make sure to use our logo as well as the pictures below (use as many as you like).

Also please make sure to add our contact info:

4-18 236th st.
Fernbrook NY, 10992

718-555-0417

contact@bramblefit-example.com

Lastly please make sure to add a "Contact us for a free trial!" stamp somewhere on the page.

```html
<!DOCTYPE html>
<html lang="en">
<head>
<meta charset="utf-8">
<title>Bramble Fitness – Personal Training Flyer</title>
<link rel="stylesheet" href="https://fonts.googleapis.com/css2?family=Roboto+Condensed:wght@400;700;800&display=swap">
<style>
  :root {
    --stage: #161616;
    --white: #ffffff;
    --ink: #1f1f1f;
    --leaf: #8dc63f;
    --body-grey: #c9ccd2;
    --navy-top: #1f3a5c;
    --navy-bottom: #0c1a2b;
    --plum-top: #74124a;
    --plum-bottom: #2e0519;
    --accent-blue: #1f8ad8;
    --accent-pink: #e8178f;
    --contact-blue: #3aa0e8;
    --contact-pink: #f0399f;
  }
  * { box-sizing: border-box; margin: 0; padding: 0; }
  html, body {
    width: 1200px; height: 1000px; overflow: hidden;
    background: var(--stage);
    font-family: "Roboto Condensed", "Arial Narrow", sans-serif;
  }
  .stage {
    position: relative; width: 1200px; height: 1000px;
    display: flex; justify-content: center; align-items: center; gap: 60px;
  }
  .flyer {
    position: relative; width: 420px; height: 860px; overflow: hidden;
    background: linear-gradient(180deg, var(--bg-top), var(--bg-bottom));
    box-shadow: 0 10px 30px rgba(0,0,0,.5);
  }
  .flyer--navy { --bg-top: var(--navy-top); --bg-bottom: var(--navy-bottom); --accent: var(--accent-blue); --contact: var(--contact-blue); }
  .flyer--plum { --bg-top: var(--plum-top); --bg-bottom: var(--plum-bottom); --accent: var(--accent-pink); --contact: var(--contact-pink); }

  .hero-photo {
    position: absolute; left: 0; top: 60px; width: 250px; height: 580px;
    clip-path: polygon(0 0, 70% 0, 100% 45%, 85% 100%, 0 100%);
  }
  .flyer--navy .hero-photo { background: linear-gradient(160deg, #8a8176, #4f463e 60%, #2b2622); }
  .flyer--plum .hero-photo { background: linear-gradient(160deg, #5a3a32, #2a1712 60%, #150a08); }

  .brand-box {
    position: absolute; top: 0; right: 22px; width: 116px; height: 150px;
    background: var(--white);
    display: flex; flex-direction: column; align-items: center; justify-content: center; gap: 10px;
  }
  .brand-dot { width: 46px; height: 46px; border-radius: 50%; background: var(--leaf); }
  .brand-name {
    color: var(--ink); font-weight: 800; font-size: 17px; line-height: 1;
    text-transform: uppercase; text-align: center; letter-spacing: .5px;
  }

  .headline {
    position: absolute; top: 235px; right: 28px;
    color: var(--white); font-weight: 800; font-size: 64px; line-height: .92;
    text-align: right; text-transform: uppercase;
    text-shadow: -4px 3px 0 rgba(0,0,0,.55);
  }
  .intro {
    position: absolute; top: 440px; right: 28px; width: 320px;
    color: var(--body-grey); font-size: 17px; line-height: 1.3; text-align: right;
    white-space: nowrap;
  }
  .intro .try {
    display: block; color: var(--white); font-size: 22px; font-weight: 700; margin-top: 2px;
  }

  .photo-strip { position: absolute; left: 0; right: 0; top: 625px; height: 175px; display: flex; }
  .strip-photo { height: 100%; }
  .strip-photo--suspension { width: 120px; background: linear-gradient(160deg, #b58a5a, #4a3526); }
  .strip-photo--ropes { width: 165px; background: linear-gradient(170deg, #4f78b8, #9b8f86 55%, #3b3430); }
  .strip-photo--floor { width: 135px; background: linear-gradient(170deg, #dfe6ee, #8f99a3 60%, #4b525a); }

  .trial-band {
    position: absolute; left: -10px; top: 758px; width: 440px; height: 38px;
    background: var(--accent); transform: rotate(-3deg);
    display: flex; align-items: center; padding-left: 30px;
    color: var(--white); font-weight: 700; font-size: 21px;
  }
  .contact {
    position: absolute; left: 30px; top: 808px;
    color: var(--contact); font-size: 15px; font-weight: 700; line-height: 1.4;
    font-style: normal; white-space: nowrap;
  }
  .contact .sep { color: var(--white); margin: 0 4px; }
</style>
</head>
<body>
<main class="stage">
  <article class="flyer flyer--navy">
    <div class="hero-photo" role="img" aria-label="Photo of a muscular man's torso and arm"></div>
    <div class="brand-box"><span class="brand-dot"></span><span class="brand-name">Bramble<br>Fitness</span></div>
    <h1 class="headline">Your<br>Personal<br>Training</h1>
    <p class="intro">At Bramble Fitness,<br>our trainer will assist and gives the<br>unique experiences to make your body<br>achieves their best performance.<span class="try">Try us!</span></p>
    <div class="photo-strip">
      <div class="strip-photo strip-photo--suspension" role="img" aria-label="Photo of women training with suspension straps"></div>
      <div class="strip-photo strip-photo--ropes" role="img" aria-label="Photo of a man training with battle ropes outdoors"></div>
      <div class="strip-photo strip-photo--floor" role="img" aria-label="Photo of the gym floor with cardio machines"></div>
    </div>
    <div class="trial-band">Contact us for a free trial</div>
    <address class="contact">4-18 236th st. Fernbrook NY, 10992<br>718-555-0417<span class="sep">|</span>contact@bramblefit-example.com</address>
  </article>

  <article class="flyer flyer--plum">
    <div class="hero-photo" role="img" aria-label="Photo of a woman's torso in a sports top"></div>
    <div class="brand-box"><span class="brand-dot"></span><span class="brand-name">Bramble<br>Fitness</span></div>
    <h1 class="headline">Your<br>Personal<br>Training</h1>
    <p class="intro">At Bramble Fitness,<br>our trainer will assist and gives the<br>unique experiences to make your body<br>achieves their best performance.<span class="try">Try us!</span></p>
    <div class="photo-strip">
      <div class="strip-photo strip-photo--suspension" role="img" aria-label="Photo of women training with suspension straps"></div>
      <div class="strip-photo strip-photo--ropes" role="img" aria-label="Photo of a man training with battle ropes outdoors"></div>
      <div class="strip-photo strip-photo--floor" role="img" aria-label="Photo of the gym floor with cardio machines"></div>
    </div>
    <div class="trial-band">Contact us for a free trial</div>
    <address class="contact">4-18 236th st. Fernbrook NY, 10992<br>718-555-0417<span class="sep">|</span>contact@bramblefit-example.com</address>
  </article>
</main>
</body>
</html>
```